KVO-Business Card Design

I need a modern, professional business card design that includes my logo as the main feature, maybe the entire background with the contact info overlaying or even contact info on the back and the logo full frontal

Neat and organized placement of contact information

Would like to see options in black and white

Target Market(s)

real estate Developers, Construction managers, business and home owners

Industry/Entity Type

Construction

Contact Information for Business Card

KVO Construction
Danny Ferrante
General Contractor

Office: 1-888-902-7315 Ext #1
Cell: 215-730-4162
Fax: 1-888-902-7315

Font styles to use
Serif

Requirements
Must have
• title
• office #
• cell #
• Email
• website
Nice to have
• fax

```html
<!DOCTYPE html>
<html lang="en">
<head>
<meta charset="utf-8">
<title>KVO Construction – Business Cards</title>
<link rel="stylesheet" href="https://fonts.googleapis.com/css2?family=Questrial&display=swap">
<style>
  :root {
    --bg: #2b2b2b;
    --card-dark-center: #4a4a4a;
    --card-dark-edge: #0d0d0d;
    --card-light: #b3b3b3;
    --skyline: #8a8a8a;
    --ink-light: #f2f2f2;
    --ink-muted: #c9c9c9;
    --ink-dark: #1c1c1c;
    --footer-ink: #e6e6e6;
  }
  * { margin: 0; padding: 0; box-sizing: border-box; }
  html, body {
    width: 1200px; height: 799px; overflow: hidden;
    background: var(--bg);
    font-family: "Questrial", "Century Gothic", sans-serif;
  }
  .canvas {
    position: relative; width: 1200px; height: 799px;
  }
  .card {
    position: absolute; top: 250px;
    width: 520px; height: 300px;
    border-radius: 22px; overflow: hidden;
    box-shadow: 0 18px 40px rgba(0,0,0,.55);
  }
  /* Contact side */
  .card--contact {
    left: 50px;
    background: radial-gradient(ellipse at 35% 45%, var(--card-dark-center) 0%, #262626 45%, var(--card-dark-edge) 100%);
    color: var(--ink-light);
  }
  .company-title {
    position: absolute; top: 34px; right: 36px;
    font-size: 17px; letter-spacing: .5px; font-weight: 400;
    text-transform: uppercase;
  }
  .contact-block {
    position: absolute; top: 118px; left: 40px;
    display: flex; align-items: stretch; gap: 16px;
  }
  .person { text-align: right; }
  .person__name { font-size: 15px; color: var(--ink-muted); }
  .person__title { font-size: 13px; color: var(--ink-muted); margin-top: 4px; }
  .divider { width: 1px; background: var(--ink-muted); }
  .contact-list { list-style: none; font-size: 13px; color: var(--ink-muted); }
  .contact-list li { display: flex; align-items: center; gap: 8px; line-height: 20px; }
  .contact-list svg { width: 11px; height: 11px; flex: none; }
  /* Brand side */
  .card--brand {
    left: 630px;
    background: var(--card-light);
  }
  .skyline {
    position: absolute; left: 0; right: 0; bottom: 0; height: 150px;
    background: var(--skyline);
  }
  .brand-mark {
    position: absolute; top: 92px; left: 0; right: 0;
    display: flex; justify-content: center; align-items: center; gap: 12px;
    color: var(--ink-dark); font-size: 34px; letter-spacing: 1px;
  }
  .brand-mark__square { width: 22px; height: 22px; background: var(--ink-dark); }
  .brand-footer {
    position: absolute; bottom: 34px; left: 0; right: 0; text-align: center;
    color: var(--footer-ink); font-size: 10px; text-transform: uppercase; letter-spacing: .5px;
  }
</style>
</head>
<body>
<main class="canvas">
  <section class="card card--contact">
    <h2 class="company-title">KVO Construction</h2>
    <div class="contact-block">
      <div class="person">
        <p class="person__name">Danny Ferrante</p>
        <p class="person__title">(General Contractor)</p>
      </div>
      <div class="divider"></div>
      <ul class="contact-list">
        <li><svg viewBox="0 0 12 12"><circle cx="6" cy="6" r="5.3" fill="none" stroke="currentColor"/><path d="M4 3.5l1 1-.6.8a4 4 0 0 0 2.3 2.3l.8-.6 1 1-.8.8C5.5 8.5 3.5 6.5 3.2 4.3z" fill="currentColor"/></svg>Office: 1-888-902-7315 Ext #1</li>
        <li><svg viewBox="0 0 12 12"><circle cx="6" cy="6" r="5.3" fill="none" stroke="currentColor"/><rect x="4.3" y="3" width="3.4" height="6" rx=".6" fill="none" stroke="currentColor" stroke-width=".8"/></svg>Cell: 215-730-4162</li>
        <li><svg viewBox="0 0 12 12"><circle cx="6" cy="6" r="5.3" fill="none" stroke="currentColor"/><rect x="3.4" y="4.5" width="5.2" height="3.4" fill="none" stroke="currentColor" stroke-width=".8"/></svg>Fax: 1-888-902-7315</li>
      </ul>
    </div>
  </section>

  <section class="card card--brand">
    <div class="skyline" role="img" aria-label="City skyline silhouette"></div>
    <div class="brand-mark">
      <span class="brand-mark__square"></span>
      <span class="brand-mark__name">KVO Construction</span>
    </div>
    <p class="brand-footer">KVO Construction</p>
  </section>
</main>
</body>
</html>
```